Varnek Modellwerk GmbH needed a letterhead template

For English scroll down. We need a letterhead template and since we already have our logo design successfully with you, we now want to also design the letterhead with you. Down in the uploaded file you see what is important and what should definitely be seen on our template. The template should be like the homepage (www.modellwerk-varnek.example) held in red, blue and white. We need a letter-head submission. In the bottom in the chapter "databases uploading" you can find the most important things, did must be on the submission. The submission shoulderstand be in the colors blue, red and white like our homepage (www.modellwerk-varnek.example).

```html
<!DOCTYPE html>
<html lang="de">
<head>
<meta charset="utf-8">
<title>Varnek Modellwerk GmbH – Briefpapier</title>
<link href="https://fonts.googleapis.com/css2?family=Lato:wght@400;700&display=swap" rel="stylesheet">
<style>
  :root {
    --brand-blue: #1e69b4;
    --brand-red: #c1212a;
    --paper: #ffffff;
    --ink: #1a1a1a;
    --backdrop: #e9e6e2;
  }
  html, body {
    margin: 0;
    width: 1200px;
    height: 1200px;
    overflow: hidden;
    background: var(--backdrop);
    font-family: "Lato", sans-serif;
  }
  .letterhead {
    position: absolute;
    left: 190px;
    top: 20px;
    width: 868px;
    height: 1228px;
    background: var(--paper);
    transform: scale(0.945);
    transform-origin: 0 0;
    box-shadow: 0 6px 24px rgba(0,0,0,0.18);
    color: var(--ink);
    overflow: hidden;
  }
  .band {
    position: absolute;
    background: linear-gradient(180deg, var(--brand-blue) 0%, var(--brand-red) 50%, var(--brand-blue) 100%);
  }
  .band--top {
    left: 0;
    top: 0;
    width: 552px;
    height: 80px;
  }
  .band--bottom {
    right: 0;
    bottom: 0;
    width: 620px;
    height: 76px;
  }
  .sender {
    position: absolute;
    left: 58px;
    top: 107px;
    font-size: 13px;
    line-height: 17.5px;
    font-style: normal;
  }
  .brand {
    position: absolute;
    left: 468px;
    top: 82px;
    display: flex;
    align-items: center;
    gap: 14px;
  }
  .brand__mark {
    width: 40px;
    height: 40px;
    border-radius: 50%;
    background: var(--brand-blue);
  }
  .brand__name {
    font-size: 32px;
    font-weight: 700;
    color: var(--brand-red);
    letter-spacing: 0.2px;
  }
  .footer-col {
    position: absolute;
    top: 1062px;
    width: 300px;
    text-align: center;
    font-size: 13px;
    line-height: 17.5px;
  }
  .footer-col--management { left: 10px; }
  .footer-col--contact { left: 305px; }
  .footer-col--bank { left: 589px; }
</style>
</head>
<body>
  <main class="letterhead">
    <div class="band band--top" role="img" aria-label="Dekorative Kopfleiste in Blau und Rot"></div>

    <address class="sender">
      Varnek Modellwerk GmbH<br>
      Lindenweg 12<br>
      4820 Bergtal, Tirol<br>
      Österreich
    </address>

    <div class="brand">
      <span class="brand__mark"></span>
      <span class="brand__name">Varnek Modellwerk</span>
    </div>

    <div class="footer-col footer-col--management">
      Geschäftsführer Dr. Halvorsen Mira<br>
      Lindenweg 12<br>
      4820 Bergtal, Tirol<br>
      Österreich
    </div>
    <div class="footer-col footer-col--contact">
      Telefon: 0800 XX XX XX<br>
      Mail: kontakt@modellwerk-varnek.example<br>
      Web: www.modellwerk-varnek.example
    </div>
    <div class="footer-col footer-col--bank">
      Bank XXXX<br>
      IBAN: ATXX XXXX XXXX XXXX<br>
      BIC: XXXX<br>
      UID-Nr.: ATUXXXXXX
    </div>

    <div class="band band--bottom" role="img" aria-label="Dekorative Fußleiste in Blau und Rot"></div>
  </main>
</body>
</html>
```